'Cradle Ahead' promotional brochure

We have designed a 6 week program to educate impending first-time parents about the things they need to know to survive the first 6 months. Sessions delivered by general practitioner/family doctor, dietician, physiotherapist, speech pathologist and psychologist. Our promotional blurb is: 'A comprehensive education program for first-time parents-to-be, delivered over 6 weeks by health professionals in your community, about everything you need to know to look after your baby (and yourself!) in the first 6 months'. I now want to put together a promotional brochure to be distributed to those couples who express an interest which will provide further details of what will be delivered in the course.
Updates
In terms of layout, I envisaged a double sided A4 size, foldable into 3 sections, but very happy to be guided on this.
Target Market(s)
To appeal to a young, well educated demographic. First time parents couples.
Industry/Entity Type
Medical
Font styles to use
Other font styles liked:
- Playfair Display
Requirements
Must have
- Playfair display font to be consistent with our logo (attached). Logo also included please. Some consistency with colours of logo please.
Nice to have
- I am a doctor, and have no creative genes! But prefer a clean and professional appearance overall. Not too cluttered in overall appearance.
Should not have
- No cheesy pictures of babies.

```html
<!DOCTYPE html>
<html lang="en">
<head>
<meta charset="utf-8">
<title>Cradle Ahead – Brochure</title>
<link href="https://fonts.googleapis.com/css2?family=Playfair+Display:ital,wght@0,400;0,700;0,900;1,400&display=swap" rel="stylesheet">
<style>
:root{
  --green:#5cb82e;
  --green-dark:#3f8f1a;
  --grey:#8c8c8c;
  --ink:#2b2b2b;
  --white:#ffffff;
  --canvas:#f3f3f1;
  --photo-a:#e9dcd3;
  --photo-b:#c89c84;
}
*{box-sizing:border-box;margin:0;padding:0}
html,body{width:1200px;height:1200px;overflow:hidden;background:var(--canvas);font-family:"Playfair Display",Georgia,serif;color:var(--ink)}
.spread{position:absolute;left:40px;top:204px;width:1120px;height:792px;display:flex;box-shadow:0 6px 24px rgba(0,0,0,.18)}
.page{position:relative;width:560px;height:792px;background:var(--white);overflow:hidden}

/* cover */
.cover-photo{position:absolute;left:0;top:0;width:560px;height:330px;background:radial-gradient(circle at 55% 45%,var(--photo-b),var(--photo-a) 70%)}
.cover-curve{position:absolute;left:0;top:250px;width:560px;height:130px}
.price-badge{position:absolute;left:300px;top:190px;width:170px;height:170px;border-radius:50%;background:var(--white);border:8px solid var(--green);box-shadow:0 0 0 4px var(--white),0 4px 10px rgba(0,0,0,.2);display:flex;flex-direction:column;align-items:center;justify-content:center;text-align:center;line-height:1}
.price-badge .label{font-weight:700;font-size:19px;text-transform:uppercase}
.price-badge .amount{font-weight:900;font-size:46px;margin-top:4px}
.feature-box{position:absolute;left:250px;top:372px;width:290px;height:180px;background:var(--green);border-radius:0 0 18px 18px;padding:20px 18px 0 18px;color:var(--white)}
.feature-box li{list-style:none;display:flex;gap:8px;font-size:14.5px;line-height:1.15;margin-bottom:11px}
.feature-box svg{flex:none;margin-top:2px}
.cover-title{position:absolute;left:30px;top:560px;font-weight:900;color:var(--green);line-height:.92;text-shadow:2px 2px 0 var(--green-dark),4px 5px 6px rgba(0,0,0,.25)}
.cover-title .line1{display:block;font-size:64px}
.cover-title .line2{display:block;font-size:74px;padding-left:30px}
.instrument{position:absolute;left:360px;top:656px;width:190px;height:34px;border-radius:17px;background:linear-gradient(90deg,#dfe3ea,#b7c3d6)}
.brand{position:absolute;display:flex;align-items:center;gap:10px;color:var(--green);font-weight:400;text-transform:uppercase;line-height:1.05}
.brand .mark{flex:none;width:30px;height:30px;background:var(--green)}
.brand-cover{left:372px;top:598px;font-size:15px}
.contact-band{position:absolute;left:0;top:715px;width:270px;height:77px;background:var(--grey);color:var(--white);font-size:17px;text-align:center;padding-top:15px;line-height:1.2}
.phone-band{position:absolute;left:270px;top:700px;width:290px;height:72px;background:var(--green);color:var(--white);font-size:30px;display:flex;align-items:center;justify-content:center}

/* program page */
.program-head{position:absolute;left:0;top:34px;width:380px;height:48px;background:var(--green);color:var(--white);font-weight:700;font-size:28px;padding-left:22px;display:flex;align-items:center}
.brand-program{left:392px;top:38px;font-size:11px}
.brand-program .mark{width:24px;height:24px}
.program{position:absolute;left:22px;top:100px;width:516px;font-size:10.5px;line-height:1.32}
.week{margin-bottom:9px}
.week h3{font-weight:400;font-size:17px;color:var(--grey);display:flex;align-items:center;gap:6px}
.week h3::before{content:"";width:9px;height:9px;border-radius:50%;background:var(--green)}
.lead{color:var(--green);font-weight:700;font-size:11px}
.session b{font-weight:400;font-size:13px}
.topics{display:flex;flex-wrap:wrap;gap:2px 12px}
.topics span::after{content:" ✓";color:var(--green)}
.program-foot{position:absolute;left:0;bottom:0;width:560px;height:24px;background:var(--green)}
</style>
</head>
<body>
<div class="spread">
  <section class="page cover">
    <div class="cover-photo" role="img" aria-label="Photo of a parent's hands cradling a newborn's feet"></div>
    <svg class="cover-curve" viewBox="0 0 560 130" preserveAspectRatio="none">
      <path d="M0 95 Q280 80 560 5 L560 25 Q280 105 0 125 Z" fill="var(--green)"/>
      <path d="M0 125 Q280 105 560 25 L560 130 L0 130 Z" fill="var(--white)"/>
    </svg>
    <div class="price-badge"><span class="label">Total<br>Cost</span><span class="amount">$300</span></div>
    <ul class="feature-box">
      <li><svg width="12" height="12" viewBox="0 0 12 12"><rect x=".5" y=".5" width="11" height="11" fill="none" stroke="#fff"/><path d="M2.5 6l2.5 2.5 4.5-5" fill="none" stroke="#fff" stroke-width="1.5"/></svg>A Comprehensive Education Program for First Time Parents.</li>
      <li><svg width="12" height="12" viewBox="0 0 12 12"><rect x=".5" y=".5" width="11" height="11" fill="none" stroke="#fff"/><path d="M2.5 6l2.5 2.5 4.5-5" fill="none" stroke="#fff" stroke-width="1.5"/></svg>Delivered Over 6 Weeks by Health Professionals in Your Community</li>
      <li><svg width="12" height="12" viewBox="0 0 12 12"><rect x=".5" y=".5" width="11" height="11" fill="none" stroke="#fff"/><path d="M2.5 6l2.5 2.5 4.5-5" fill="none" stroke="#fff" stroke-width="1.5"/></svg>Everything You Need to Know to Look After Your baby (And Yourself!) IN THE FIRST 6 MONTHS.</li>
    </ul>
    <h1 class="cover-title"><span class="line1">CRADLE</span><span class="line2">AHEAD</span></h1>
    <div class="instrument" role="img" aria-label="Illustration of a stethoscope"></div>
    <div class="brand brand-cover"><span class="mark"></span><span>Wattle Grove<br>Health &amp;<br>Medical</span></div>
    <div class="contact-band">Contact details for enquiries<br>bookings</div>
    <div class="phone-band">(02) 5550 1234</div>
  </section>

  <section class="page program-page">
    <h2 class="program-head">‘CRADLE AHEAD’</h2>
    <div class="brand brand-program"><span class="mark"></span><span>Wattle Grove<br>Health &amp; Medical</span></div>
    <div class="program">
      <div class="week"><h3>Week 1</h3>
        <p class="lead">GP Dr Hannah Morrow will share information for Mum's own health after delivery. Topics include:</p>
        <p class="topics"><span>Bleeding, bladder and bowel after delivery</span><span>Breastfeeding, engorgement and mastitis</span><span>Vaccinations in pregnancy</span><span>Bottle feeding</span><span>Post-natal anxiety &amp; depression</span><span>Intimacy and contraception</span></p></div>
      <div class="week"><h3>Week 2</h3>
        <p class="session"><b>Session 1</b> – Clinical Psychologist Dr Renee Calder will discuss changes in relationships as couples become parents, gender roles in parenting and post-natal depression.</p>
        <p class="session"><b>Session 2</b> – Physiotherapist Tessa Hartley will present advice for Mums regarding exercise during and after pregnancy, looking after the pelvic floor during and after pregnancy, and abdominal muscle separation management. She will also provide advice for promoting babies' neck strength and minimising the risk of flat spots on the head and encouraging gross motor skills in the first 6 months.</p></div>
      <div class="week"><h3>Week 3</h3>
        <p class="session"><b>Session 1</b> – Dietician Amy Lindqvist provides advice for Mums regarding healthy eating during pregnancy and lactation, normal weight gain during pregnancy and realistic weight loss after. She will also discuss the evidence regarding breastfeeding vs bottle-feeding, normal infant weight gain and introducing solids (including those with potential for allergy).</p>
        <p class="session"><b>Session 2</b> – Paediatric Speech Pathologist Claire Bowden will share information about latching and breast-feeding troubles &amp; tongue tie, advice about dummies and finger-sucking, introducing solids &amp; feeding (including 'pouch' food), encouraging language development and current evidence about electronic devices impacting language development.</p></div>
      <div class="week"><h3>Week 4</h3>
        <p class="lead">GP Dr Hannah Morrow will share advice about your babies' health in the first 6 months, including:</p>
        <p class="topics"><span>Skin of newborns</span><span>Sleeping</span><span>Crying</span><span>Immunisations</span><span>Fever and infections</span><span>Diarrhoea and constipation</span><span>Teething</span><span>Understanding a baby's signals</span></p></div>
      <div class="week"><h3>Week 5</h3>
        <p class="session"><b>Session 1</b> – Clinical Psychologist Dr Renee Calder will share information about bonding &amp; attachment with your baby, how to promote their social &amp; emotional development and how to manage separation anxiety. She will also discuss positive parenting approaches.</p></div>
      <div class="week"><h3>Week 6</h3>
        <p class="session"><b>Session 1</b> – Secret Men's Business – a men-only session (including beer!) with a new father for frank discussion about the road ahead. Mums will do a shopping excursion with the GP &amp; Dietician to Freshway to look at baby products and food – the good and the bad!</p>
        <p class="session"><b>Session 2</b> – Program review, reflection and evaluation and future session planning when baby is 6 months of age.</p></div>
    </div>
    <div class="program-foot"></div>
  </section>
</div>
</body>
</html>
```